New letterhead design for legal, public interest law firm

THIS IS FOR A LETTERHEAD DESIGN CONTEST , PLEASE REFRAIN FROM SUBMITTING JUST LOGO PROPOSALS AND BUSINESS CARD. LOGO AND BUSINESS CARD PROJECTS WILL BE AWARDED TO THE WINNER OF THE LETTERHEAD DESIGN.
Looking for a timeless, elegant and modern design for our letterhead and logo. Our website is www.lmrkvoa.org so you can incorporate the mission, vision and values into the design. As we also included a request for a NEW LOGO design, please be sure to include logo design options.
We are a public interest criminal defense organization that represents indigent people charged with federal crimes. Please weave the mission/vision/values and our practice area into the logo design.
Target Market(s)
Judges, clients, attorneys, family members of our clients.
Industry/Entity Type
Legal
Contact Information for Business Card
Include line for address, direct line, fax, email address, website address. Remember to incorporate NEW LOGO design.
Logo Text
Coastal Legal Advocacy Collective of the Western Valley
Requirements
Must have
- Please remember this project is also to design us a NEW LOGO. Please do not incorporate the existing logo into the new letterhead design.
Nice to have
- Nice to see some logo samples incorporating symbolism for justice, California specific imagery.
Should not have
- New logo should NOT have any traditional/typical legal related images (e.g., scales of justice, etc.)

```html
<!DOCTYPE html>
<html lang="en">
<head>
<meta charset="utf-8">
<title>Letterhead – Coastal Legal Advocacy Collective of the Western Valley</title>
<link rel="stylesheet" href="https://fonts.googleapis.com/css2?family=Mulish:wght@300;400;600;700&display=swap">
<style>
  :root {
    --navy: #27399a;
    --orange: #f59a23;
    --tint: #e9ecf4;
    --ink: #4a4a4f;
    --muted: #8a8a90;
    --paper: #ffffff;
    --stage: #e4e4e6;
  }
  * { box-sizing: border-box; margin: 0; padding: 0; }
  html, body {
    width: 1200px; height: 936px; overflow: hidden;
    background: var(--stage);
    font-family: "Mulish", sans-serif;
    color: var(--ink);
  }
  .letterhead {
    position: absolute;
    left: 269px; top: 34px;
    width: 662px; height: 868px;
    background: var(--paper);
    box-shadow: 0 2px 10px rgba(0,0,0,0.08);
    overflow: hidden;
  }
  .brand {
    position: absolute; left: 44px; top: 52px;
    display: flex; align-items: center; gap: 12px;
    width: 300px;
  }
  .brand-square {
    flex: none; width: 46px; height: 46px; background: var(--navy);
  }
  .brand-name {
    font-weight: 700; font-size: 13px; line-height: 1.3;
    color: var(--navy); text-transform: uppercase; letter-spacing: 0.08em;
  }
  .date-line {
    position: absolute; left: 44px; top: 134px;
    font-size: 10px; letter-spacing: 0.12em; color: var(--ink);
  }
  .date-line .dots { letter-spacing: 0.2em; color: var(--muted); }
  .backdrop-panel {
    position: absolute; left: 150px; top: 176px;
    width: 362px; height: 362px; background: var(--tint);
  }
  .closing {
    position: absolute; right: 70px; top: 540px;
    text-align: left; width: 160px;
  }
  .closing-phrase { font-size: 12px; color: var(--ink); font-weight: 300; }
  .signature {
    margin-top: 8px; width: 130px; height: 44px;
    background: linear-gradient(90deg, #f3f3f4, #fafafa);
    border-radius: 4px;
  }
  .offices {
    position: absolute; left: 44px; right: 30px; bottom: 44px;
    display: flex; gap: 26px;
  }
  .office { flex: 1; }
  .office-city {
    font-size: 14px; font-weight: 600; color: var(--navy);
    letter-spacing: 0.03em; text-transform: uppercase;
    display: flex; align-items: center; gap: 6px; margin-bottom: 4px;
  }
  .office-city svg { width: 9px; height: 12px; }
  .office p { font-size: 8.5px; line-height: 1.45; color: var(--ink); }
  .office-phone {
    margin-top: 5px; display: flex; align-items: center; gap: 6px;
    font-size: 9px; color: var(--orange);
  }
  .phone-icon {
    width: 10px; height: 10px; background: var(--navy); border-radius: 2px;
    display: grid; place-items: center;
  }
  .phone-icon svg { width: 7px; height: 7px; }
  .base-band { position: absolute; left: 0; right: 0; bottom: 0; height: 18px; }
  .band { position: absolute; bottom: 0; }
  .band-left { left: 0; width: 38%; height: 9px; background: var(--navy); }
  .band-mid { left: 38%; width: 30%; height: 18px; background: var(--orange); }
  .band-right { left: 68%; right: 0; height: 9px; background: var(--navy); }
</style>
</head>
<body>
  <main class="letterhead">
    <header class="brand">
      <span class="brand-square"></span>
      <span class="brand-name">Coastal Legal Advocacy Collective of the Western Valley</span>
    </header>

    <div class="date-line">DATE : <span class="dots">..............</span></div>

    <div class="backdrop-panel" aria-hidden="true"></div>

    <div class="closing">
      <p class="closing-phrase">Yours faithfully</p>
      <div class="signature" role="img" aria-label="Handwritten signature"></div>
    </div>

    <footer class="offices">
      <section class="office">
        <h2 class="office-city">North Bay
          <svg viewBox="0 0 10 14"><path d="M5 0a5 5 0 0 0-5 5c0 4 5 9 5 9s5-5 5-9a5 5 0 0 0-5-5zm0 7a2 2 0 1 1 0-4 2 2 0 0 1 0 4z" fill="var(--navy)"/></svg>
        </h2>
        <p>48 Harbor Row<br>North Bay, California 90010<br>Chief Deputy: Daniel Reyes Moll<br>Administrative Officer: Ivy Tarrant</p>
        <div class="office-phone"><span class="phone-icon"><svg viewBox="0 0 10 10"><path d="M2 1l2 2-1 1.2c.6 1.2 1.6 2.2 2.8 2.8L7 6l2 2-1.2 1.5C4.5 9.2.8 5.5.5 2.2z" fill="#fff"/></svg></span>(555) 014-2854</div>
      </section>
      <section class="office">
        <h2 class="office-city">Eastfield
          <svg viewBox="0 0 10 14"><path d="M5 0a5 5 0 0 0-5 5c0 4 5 9 5 9s5-5 5-9a5 5 0 0 0-5-5zm0 7a2 2 0 1 1 0-4 2 2 0 0 1 0 4z" fill="var(--navy)"/></svg>
        </h2>
        <p>920 Orchard Avenue<br>Suite 410<br>Eastfield, California 92020<br>Directing Attorney: Marisol Vantreece<br>Branch Admin. Asst.: June Calloway</p>
        <div class="office-phone"><span class="phone-icon"><svg viewBox="0 0 10 10"><path d="M2 1l2 2-1 1.2c.6 1.2 1.6 2.2 2.8 2.8L7 6l2 2-1.2 1.5C4.5 9.2.8 5.5.5 2.2z" fill="#fff"/></svg></span>(555) 017-6346</div>
      </section>
      <section class="office">
        <h2 class="office-city">South Point
          <svg viewBox="0 0 10 14"><path d="M5 0a5 5 0 0 0-5 5c0 4 5 9 5 9s5-5 5-9a5 5 0 0 0-5-5zm0 7a2 2 0 1 1 0-4 2 2 0 0 1 0 4z" fill="var(--navy)"/></svg>
        </h2>
        <p>702 West Mill Street<br>South Point, California 92730<br>Directing Attorney: Nora Kestrel<br>Branch Admin. Asst.: Leah Dorsey</p>
        <div class="office-phone"><span class="phone-icon"><svg viewBox="0 0 10 10"><path d="M2 1l2 2-1 1.2c.6 1.2 1.6 2.2 2.8 2.8L7 6l2 2-1.2 1.5C4.5 9.2.8 5.5.5 2.2z" fill="#fff"/></svg></span>(555) 019-4500</div>
      </section>
    </footer>

    <div class="base-band" aria-hidden="true">
      <span class="band band-left"></span>
      <span class="band band-mid"></span>
      <span class="band band-right"></span>
    </div>
  </main>
</body>
</html>
```